Event Poster - Tarona Mist Fest 2018 (Need ASAP)

Create a poster for an upcoming vape event, located in Tarona, Hamilton, New Zealand.

Mist Fest is an event where lots of shops come to a location, and the public are welcomed and they all vape, buy vape products, socialize, drink beer and have fun.

VISIT THE EVENT WEBSITE FOR INFO - www.taronamistfest.co.nz

We have created a website at, as you can see the logo and design is a bit boring and plain, so we dont really want it to look anything like that, The logo that is created to suit the poster will be able to be

Need a poster done up so we can send it around, post it up on boards, share on social media etc

I have attached previous events from nearby towns, for reference, but I want something much better.

Target Market(s)

25-45 Male / Female

Requirements
Must have
• - Tarona Mist Fest 2018
• - Saturday, 2nd June 2018
• - 12-10pm
• - R18 Event (important for public to know)
• - Vendors, Prizes, Comps, E Juice Awards, Entertainment, Giveaways & More
• - The Corner Alehouse (52 Mulgrave Rd, Kerepuni, Hamilton)
• - mention something along lines "Come To Tarona's First Mist Fest"
• - "Get Your Tickets from www.taronamistfest.co.nz TODAY"
• - I want people to know they can buy it from a store as well "The Cloud Barn"
Nice to have
• Our City colors are Red,Yellow,Black which is symbolic for "Tarona" so it would be nice to have those integrated in there. Alot of the other Mist Fest events have dark, bogan, amateur look done to them, so I want ours to be just a much better version.
• To Clarify, Hamilton is a city inside the Tarona
• I might want to put sponsors on there as well, possibly 10-20, but maybe only a few if space is a problem

```html
<!DOCTYPE html>
<html lang="en">
<head>
<meta charset="utf-8">
<title>Tarona Mist Fest 2018</title>
<link href="https://fonts.googleapis.com/css2?family=Montserrat:wght@300;400;600;800;900&family=Oswald:wght@400;500&family=Righteous&display=swap" rel="stylesheet">
<style>
  :root{
    --red:#d8141f;
    --red-deep:#8a0f1c;
    --ink:#120a0f;
    --white:#ffffff;
    --yellow:#f2c51a;
    --lime:#d6e81c;
  }
  *{box-sizing:border-box;margin:0;padding:0}
  html,body{width:891px;height:1200px;overflow:hidden;background:var(--ink)}
  .poster{position:relative;width:891px;height:1200px;overflow:hidden;font-family:"Montserrat",sans-serif;color:var(--white)}
  .hero-photo{position:absolute;inset:0;
    background:
      radial-gradient(ellipse 260px 200px at 640px 120px,rgba(233,214,224,.55),transparent 70%),
      radial-gradient(ellipse 300px 140px at 330px 520px,rgba(233,214,224,.45),transparent 70%),
      radial-gradient(ellipse 340px 520px at 200px 420px,#b01d2c,transparent 75%),
      radial-gradient(ellipse 200px 140px at 260px 880px,rgba(216,20,31,.7),transparent 75%),
      linear-gradient(160deg,#7e1625 0%,#521024 40%,#2b0a17 75%,#150a10 100%);}
  .abs{position:absolute;white-space:nowrap}
  h1{font-size:inherit}
  .r18{left:560px;top:36px;width:150px;text-align:center}
  .r18 .mark{font-family:"Righteous",sans-serif;font-size:62px;line-height:1;color:var(--red);-webkit-text-stroke:2px var(--white)}
  .r18 .sub{font-size:24px;letter-spacing:7px;font-weight:400;color:var(--ink);line-height:1.1}
  .title{font-weight:900;color:var(--white);line-height:.85;text-align:right;right:30px}
  .title-city{top:150px;font-size:92px;letter-spacing:-2px;color:transparent;-webkit-text-stroke:3px var(--white)}
  .title-main{top:236px;font-size:226px;letter-spacing:-10px}
  .title-end{top:462px;font-size:140px;letter-spacing:-4px;color:transparent;-webkit-text-stroke:4px var(--white)}
  .title-year{top:596px;right:44px;font-size:84px;font-weight:800;color:var(--lime);letter-spacing:-3px;line-height:1}
  .date{right:40px;text-align:right;line-height:1}
  .date-day{top:698px;font-size:36px;font-weight:400;letter-spacing:-1px}
  .date-num{top:735px;font-size:82px;font-weight:800;color:transparent;-webkit-text-stroke:3px var(--white)}
  .date-month{top:813px;font-size:60px;font-weight:800;color:var(--yellow)}
  .time{top:878px;right:42px;font-family:"Righteous",sans-serif;font-size:22px;line-height:24px;color:var(--red);display:flex;align-items:center;gap:6px}
  .venue{top:907px;right:42px;font-family:"Righteous",sans-serif;font-size:25px;line-height:28px;color:var(--yellow);display:flex;align-items:center;gap:8px}
  .address{top:939px;right:42px;font-size:14px;line-height:16px;font-weight:600;letter-spacing:.3px}
  .divider{left:400px;top:962px}
  .features{top:983px;right:42px;text-align:right;font-family:"Righteous",sans-serif;font-size:23px;letter-spacing:2px;line-height:28px}
  .features .w{color:var(--white)} .features .r{color:var(--red)} .features .y{color:var(--yellow)}
  .invite{left:40px;top:903px}
  .invite-lead{font-size:36px;line-height:36px;font-weight:300;color:var(--yellow)}
  .invite-city{font-size:50px;line-height:52px;font-weight:900;margin-top:2px}
  .invite-tail{font-size:40px;line-height:42px;font-weight:300;margin-top:2px}
  .invite-tail b{font-weight:900}
  .invite-tail span{color:var(--yellow)}
  .ticket-pill{left:5px;top:1044px;width:410px;height:46px;background:linear-gradient(90deg,var(--red-deep),var(--red));border-radius:0 12px 12px 0;font-family:"Oswald",sans-serif;font-size:28px;line-height:46px;padding-left:36px;color:var(--white)}
  .ticket-pill span{color:var(--yellow)}
  .event-mark{left:40px;top:1118px;display:flex;align-items:center;gap:8px;font-family:"Oswald",sans-serif;font-size:16px;font-weight:500;color:var(--yellow);line-height:1.05;white-space:normal;width:140px}
  .event-mark i{display:block;width:32px;height:50px;background:var(--yellow);flex:none}
  .shop{left:190px;top:1118px;text-align:center;font-family:"Oswald",sans-serif;line-height:1.2}
  .shop-name{font-size:24px;font-weight:500}
  .shop-offer{font-size:16px}
  .web{right:46px;top:1117px;font-family:"Oswald",sans-serif;font-size:16px;line-height:20px;font-weight:400}
  .web b{color:var(--yellow);font-weight:400}
  .web em{color:var(--red);font-style:normal;font-weight:500;margin-left:6px}
  .store-bar{left:398px;top:1144px;width:482px;height:32px;background:var(--yellow);color:var(--ink);font-family:"Oswald",sans-serif;font-size:19px;line-height:32px;padding-left:26px;transform:skewX(-12deg)}
  .store-bar span{display:block;transform:skewX(12deg)}
</style>
</head>
<body>
<main class="poster">
  <div class="hero-photo" role="img" aria-label="Photo of a man in a red cap and track jacket exhaling a cloud of vapour, with glowing e-liquid dropper bottles in front and pink smoke drifting across"></div>

  <div class="abs r18"><div class="mark">R18</div><div class="sub">EVENT</div></div>

  <h1>
    <span class="abs title title-city">TARONA</span>
    <span class="abs title title-main">MIST</span>
    <span class="abs title title-end">FEST</span>
    <span class="abs title-year">2018</span>
  </h1>

  <div class="abs date date-day">SATURDAY</div>
  <div class="abs date date-num">2ND</div>
  <div class="abs date date-month">JUNE</div>

  <div class="abs time">
    <svg width="18" height="18" viewBox="0 0 18 18"><circle cx="9" cy="9" r="7.5" fill="none" stroke="#fff" stroke-width="1.6"/><path d="M9 4.5V9h3.5" fill="none" stroke="#fff" stroke-width="1.6"/></svg>
    12-10PM
  </div>
  <div class="abs venue">
    <svg width="18" height="24" viewBox="0 0 18 24"><path d="M9 1a8 8 0 0 0-8 8c0 6 8 14 8 14s8-8 8-14a8 8 0 0 0-8-8z" fill="#d8141f"/><circle cx="9" cy="9" r="3" fill="#120a0f"/></svg>
    THE CORNER ALEHOUSE
  </div>
  <div class="abs address">52 MULGRAVE RD, KEREPUNI, HAMILTON</div>

  <svg class="abs divider" width="460" height="30" viewBox="0 0 460 30"><path d="M0 29H95L125 3H450" fill="none" stroke="#d6e81c" stroke-width="1.2"/></svg>

  <div class="abs features">
    <div class="w">VENDORS, PRIZES,</div>
    <div class="r">COMPS, E JUICE AWARDS,</div>
    <div class="y">ENTERTAINMENT,</div>
    <div class="w">GIVEAWAYS &amp; MORE</div>
  </div>

  <div class="abs invite">
    <div class="invite-lead">COME TO</div>
    <div class="invite-city">TARONA'S</div>
    <div class="invite-tail"><span>FIRST</span> <b>MIST</b> FEST</div>
  </div>

  <div class="abs ticket-pill"><span>TICKETS AVAILABLE</span> AT COUNTER</div>

  <div class="abs event-mark"><i></i>TARONA MIST FEST 2018</div>

  <div class="abs shop">
    <div class="shop-name">THE CLOUD BARN</div>
    <div class="shop-offer">BUY TODAY FOR $20</div>
  </div>

  <div class="abs web">Get Your Tickets from <b>www.taronamistfest.co.nz</b><em>TODAY</em></div>
  <div class="abs store-bar"><span>TICKETS ARE AVAILABLE TO BUY IN STORE</span></div>
</main>
</body>
</html>
```